big banner for travel agency 70cm x 183cm

We are a travel agency specializing in air ticketing, tours,transport and hotel bookings for both domestic and international destinations.We need a banner 70cm (width) x 183cm (length) for our store front. This should be bold, professional, and have a great visual impact.
Some words and their translations are required as attached. Please make sure they are printed in the same font.
Target Market(s)
tourists, travelers, local population who require our services
Industry/Entity Type
Travel Industry
Font styles to use
Sans Serif
Other font styles liked:
- impact
Requirements
Must have
- words as attached in ms word.
- name of travel agency: PDW Travel N Services
- tagline : Explore. Discover. Dream
- Services: Ticketing, Transport, Tours & Hotel Bookings
- 300 Airlines
- 100 Tours Worldwide
- 100,000 Hotel Partners
Nice to have
- creative yet professional with great visual impact

```html
<!DOCTYPE html>
<html lang="en">
<head>
<meta charset="utf-8">
<title>Travel Services Storefront Banner</title>
<link rel="stylesheet" href="https://fonts.googleapis.com/css2?family=Anton&family=Source+Sans+3:wght@400;600;700&family=Noto+Sans+KR:wght@300&family=Noto+Sans+SC:wght@300&display=swap">
<style>
  :root {
    --backdrop: #2b2b2b;
    --teal: #33ada5;
    --red: #e0314b;
    --circle: #e5e5e5;
    --stats-bg: #e8e8e8;
    --stats-text: #4a4a4a;
    --footer-bg: #141414;
    --tagline: #e8405a;
    --white: #ffffff;
    --divider: rgba(255,255,255,0.45);
  }
  html, body {
    margin: 0;
    padding: 0;
    width: 701px;
    height: 1200px;
    overflow: hidden;
    background: var(--backdrop);
  }
  .banner {
    position: absolute;
    left: 161.6px;
    top: 105.6px;
    width: 378.4px;
    height: 987.2px;
    display: block;
  }
  .latin { font-family: "Source Sans 3", sans-serif; }
  .korean { font-family: "Noto Sans KR", sans-serif; font-weight: 300; }
  .chinese { font-family: "Noto Sans SC", sans-serif; font-weight: 300; }
  .stat { font-family: "Anton", sans-serif; }
  .stat-number { fill: var(--red); }
  .stat-label { fill: var(--stats-text); }
</style>
</head>
<body>
<svg class="banner" viewBox="0 0 378.4 987.2" xmlns="http://www.w3.org/2000/svg" role="img" aria-label="Travel services storefront banner">
  <!-- Welcome header -->
  <rect class="welcome-band" x="0" y="0" width="378.4" height="213.6" fill="var(--teal)"/>
  <g class="welcome-text" fill="var(--white)" text-anchor="middle">
    <text class="latin" x="192" y="77" font-size="41" font-weight="700" textLength="184" lengthAdjust="spacingAndGlyphs">WELCOME</text>
    <text class="korean" x="196" y="125" font-size="40" textLength="203" lengthAdjust="spacingAndGlyphs">환영합니다</text>
    <text class="chinese" x="192" y="179" font-size="42" textLength="165" lengthAdjust="spacingAndGlyphs">欢迎光临</text>
  </g>

  <!-- Services -->
  <rect class="services-band" x="0" y="213.6" width="378.4" height="501.6" fill="var(--red)"/>

  <g class="service service-air">
    <circle cx="104.8" cy="300.8" r="62.4" fill="var(--circle)"/>
    <g class="icon-plane" fill="var(--teal)" transform="translate(104.8 300.8) rotate(45)">
      <path d="M-4 -30 Q0 -38 4 -30 L4 -6 L30 8 L30 14 L4 6 L4 22 L12 28 L12 32 L0 29 L-12 32 L-12 28 L-4 22 L-4 6 L-30 14 L-30 8 L-4 -6 Z"/>
    </g>
    <g fill="var(--white)">
      <text class="latin" x="198.4" y="269" font-size="32" textLength="144" lengthAdjust="spacingAndGlyphs">Air Tickets</text>
      <text class="korean" x="198.4" y="309" font-size="33" textLength="99" lengthAdjust="spacingAndGlyphs">항공권</text>
      <text class="chinese" x="198.4" y="354" font-size="34" textLength="68" lengthAdjust="spacingAndGlyphs">机票</text>
    </g>
  </g>

  <line class="divider" x1="56.8" y1="384" x2="340" y2="384" stroke="var(--divider)" stroke-width="1.2"/>

  <g class="service service-tours">
    <circle cx="104.8" cy="467.2" r="62.4" fill="var(--circle)"/>
    <g class="icon-suitcase" fill="var(--teal)">
      <rect x="75.8" y="448" width="58" height="41" rx="5"/>
      <path d="M94 448 v-7 a3 3 0 0 1 3 -3 h15.6 a3 3 0 0 1 3 3 v7 h-4 v-6 h-13.6 v6 z"/>
      <rect x="84" y="448" width="2" height="41" fill="var(--circle)"/>
      <rect x="123.6" y="448" width="2" height="41" fill="var(--circle)"/>
    </g>
    <g fill="var(--white)">
      <text class="latin" x="198.4" y="437" font-size="32" textLength="78" lengthAdjust="spacingAndGlyphs">Tours</text>
      <text class="korean" x="198.4" y="477" font-size="33" textLength="64" lengthAdjust="spacingAndGlyphs">투어</text>
      <text class="chinese" x="198.4" y="522" font-size="34" textLength="68" lengthAdjust="spacingAndGlyphs">旅游</text>
    </g>
  </g>

  <line class="divider" x1="56.8" y1="556" x2="340" y2="556" stroke="var(--divider)" stroke-width="1.2"/>

  <g class="service service-hotels">
    <circle cx="104.8" cy="636" r="62.4" fill="var(--circle)"/>
    <g class="icon-building">
      <rect x="82" y="610" width="46" height="56" fill="var(--teal)"/>
      <g fill="var(--circle)">
        <rect x="88" y="616" width="4" height="4"/><rect x="96" y="616" width="4" height="4"/><rect x="104" y="616" width="4" height="4"/><rect x="112" y="616" width="4" height="4"/><rect x="120" y="616" width="4" height="4"/>
        <rect x="88" y="625" width="4" height="4"/><rect x="96" y="625" width="4" height="4"/><rect x="104" y="625" width="4" height="4"/><rect x="112" y="625" width="4" height="4"/><rect x="120" y="625" width="4" height="4"/>
        <rect x="88" y="634" width="4" height="4"/><rect x="96" y="634" width="4" height="4"/><rect x="104" y="634" width="4" height="4"/><rect x="112" y="634" width="4" height="4"/><rect x="120" y="634" width="4" height="4"/>
        <rect x="88" y="643" width="4" height="4"/><rect x="96" y="643" width="4" height="4"/><rect x="104" y="643" width="4" height="4"/><rect x="112" y="643" width="4" height="4"/><rect x="120" y="643" width="4" height="4"/>
        <rect x="99" y="654" width="12" height="12"/>
      </g>
    </g>
    <g fill="var(--white)">
      <text class="latin" x="198.4" y="606" font-size="32" textLength="90" lengthAdjust="spacingAndGlyphs">Hotels</text>
      <text class="korean" x="198.4" y="646" font-size="33" textLength="64" lengthAdjust="spacingAndGlyphs">호텔</text>
      <text class="chinese" x="198.4" y="690" font-size="34" textLength="68" lengthAdjust="spacingAndGlyphs">酒店</text>
    </g>
  </g>

  <!-- Key figures -->
  <rect class="stats-band" x="0" y="715.2" width="378.4" height="209.6" fill="var(--stats-bg)"/>
  <g class="stats">
    <text class="stat" x="60" y="785" font-size="50" textLength="257" lengthAdjust="spacingAndGlyphs"><tspan class="stat-number">300</tspan> <tspan class="stat-label">AIRLINES</tspan></text>
    <text class="stat" x="17.6" y="845" font-size="42" textLength="343" lengthAdjust="spacingAndGlyphs"><tspan class="stat-number">100</tspan> <tspan class="stat-label">TOURS WORLDWIDE</tspan></text>
    <text class="stat" x="4.8" y="901" font-size="42" textLength="366" lengthAdjust="spacingAndGlyphs"><tspan class="stat-number">100,000</tspan> <tspan class="stat-label">HOTEL PARTNERS</tspan></text>
  </g>

  <!-- Tagline -->
  <rect class="tagline-band" x="0" y="924.8" width="378.4" height="62.4" fill="var(--footer-bg)"/>
  <text class="latin tagline" x="188.8" y="964" font-size="20" font-weight="600" fill="var(--tagline)" text-anchor="middle" textLength="256" lengthAdjust="spacingAndGlyphs">EXPLORE. DISCOVER. DREAM</text>
</svg>
</body>
</html>
```